ultra-minimalist business card

front (black background, matte):

tarik b. hosseny
writer | photographer
get@tarikhosseny.com

back (white background, matte):

a picture speaks a thousand words;
a word draws a thousand pictures.

www.tarikhosseny.com

all text should be small (white or silver - as long as it shows against the black - on the front; black or gray - as long as it shows against the white - on the back).

feel free to get creative in terms of arrangement, alignment, and font type, but remember, the overall style is minimalist, so nothing too fancy, please.

thanks.

```html
<!DOCTYPE html>
<html lang="en">
<head>
<meta charset="utf-8">
<title>Tarik B. Hosseny – Business Card</title>
<link rel="stylesheet" href="https://fonts.googleapis.com/css2?family=Jost:ital,wght@1,500&family=Source+Sans+3:ital,wght@1,400&family=Open+Sans:wght@400&family=Cormorant+Garamond:ital,wght@1,400&display=swap">
<style>
  :root {
    --backdrop: #8f8f8f;
    --card-dark: #1c1c1c;
    --card-light: #f0f0f0;
    --ink-light: #f2f2f2;
    --ink-dark: #1c1c1c;
    --ink-quote: #6a6a6a;
  }
  * { margin: 0; padding: 0; box-sizing: border-box; }
  html, body {
    width: 980px;
    height: 1200px;
    overflow: hidden;
    background: var(--backdrop);
  }
  .card {
    position: absolute;
    left: 119px;
    width: 720px;
    height: 412px;
    overflow: hidden;
  }
  .card--front { top: 131px; background: var(--card-dark); }
  .card--back { top: 710px; background: var(--card-light); }

  .card__name {
    position: absolute;
    left: 38px;
    top: 72px;
    font-family: "Jost", sans-serif;
    font-style: italic;
    font-weight: 500;
    font-size: 46px;
    line-height: 1;
    color: var(--ink-light);
    letter-spacing: 0.2px;
  }
  .card__role {
    position: absolute;
    left: 140px;
    top: 124px;
    font-family: "Source Sans 3", sans-serif;
    font-style: italic;
    font-weight: 400;
    font-size: 29px;
    line-height: 1;
    color: var(--ink-light);
  }
  .contact-band {
    position: absolute;
    left: 399px;
    top: 313px;
    width: 321px;
    height: 56px;
    background: var(--card-light);
    display: flex;
    align-items: center;
    padding-left: 52px;
    gap: 18px;
  }
  .contact-band__icon { width: 27px; height: 30px; flex: none; }
  .contact-band__email {
    font-family: "Open Sans", sans-serif;
    font-size: 17.5px;
    color: var(--ink-dark);
    letter-spacing: 0.2px;
  }

  .card__quote {
    position: absolute;
    left: 0;
    width: 100%;
    top: 150px;
    text-align: center;
    font-family: "Cormorant Garamond", serif;
    font-style: italic;
    font-weight: 400;
    font-size: 45px;
    line-height: 62px;
    color: var(--ink-quote);
  }
  .web-band {
    position: absolute;
    left: 0;
    top: 322px;
    width: 360px;
    height: 63px;
    background: var(--card-dark);
    display: flex;
    align-items: center;
    padding-left: 46px;
  }
  .web-band__url {
    font-family: "Jost", sans-serif;
    font-style: italic;
    font-weight: 500;
    font-size: 25px;
    color: var(--ink-light);
    letter-spacing: 0.3px;
  }
</style>
</head>
<body>
  <section class="card card--front">
    <h1 class="card__name">Tarik B. Hosseny</h1>
    <p class="card__role">writer | photographer</p>
    <div class="contact-band">
      <svg class="contact-band__icon" viewBox="0 0 27 30" fill="none" stroke="#1c1c1c" stroke-width="1.4" aria-hidden="true">
        <path d="M5 13 V2 H22 V13"/>
        <path d="M9 6 H16 M9 9 H18 M9 12 H18"/>
        <path d="M1 12 L13.5 21 L26 12 V28 H1 Z"/>
        <path d="M1 28 L10.5 19 M26 28 L16.5 19"/>
      </svg>
      <span class="contact-band__email">get@tarikhosseny.com</span>
    </div>
  </section>

  <section class="card card--back">
    <p class="card__quote">a picture speaks a thousand words;<br>a word draws a thousand pictures.</p>
    <div class="web-band">
      <span class="web-band__url">www.tarikhosseny.com</span>
    </div>
  </section>
</body>
</html>
```